Nail Technician Business Card Design

My business is a nail technician business which involves applying nail enhancements to clients nails. I would like a design that uses the colours:, purple or black and silver on a light grey background. The final design should entice clients to my business.
I would like appointment times on the back of the card.
I want the spilled bottle on the front and the other one on the back
I would like the dragonfly font
Updates
Project Deadline Extended
Reason: I have found a font I would like used and also an image/logo
I have listed some ideas I would like used on the design of my card. thanks
Tessa
Industry/Entity Type
Business
Contact Information for Business Card
Lumen Nail Designs
41 Wendover street,
Carrowbrook, NSW 2791
Mobile: 0400 582 316
Tessa Harcourt
Like us on Chatterly
Font styles to use
Other font styles liked:
- Dragonfly
Look and feel
Each slider illustrates characteristics of the customer's brand and the style your logo design should communicate.

```html
<!DOCTYPE html>
<html lang="en">
<head>
<meta charset="utf-8">
<title>Lumen Nail Designs – Business Cards</title>
<link rel="stylesheet" href="https://fonts.googleapis.com/css2?family=Arimo:wght@400;700&family=Tinos&display=swap">
<style>
  :root {
    --backdrop: #2a2a2c;
    --card-light: #f1f1f2;
    --card-mid: #d9d9dc;
    --plum: #56224f;
    --charcoal: #2f2b2c;
    --ink: #2b2228;
    --fine-ink: #4a4046;
    --white: #ffffff;
    --orchid-soft: #c7a6cc;
    --orchid: #9a5f9e;
    --orchid-deep: #6d2f69;
  }
  * { margin: 0; padding: 0; box-sizing: border-box; }
  html, body {
    width: 849px; height: 1200px; overflow: hidden;
    background: var(--backdrop);
  }
  .sheet { position: relative; width: 849px; height: 1200px; }
  .card {
    position: absolute; overflow: hidden;
    background: linear-gradient(180deg, var(--card-mid) 0%, var(--card-light) 60%, var(--card-light) 100%);
    box-shadow: 0 4px 10px rgba(0,0,0,.45);
    font-family: "Arimo", Arial, sans-serif;
  }
  .card--front-land { left: 35px; top: 63px; width: 360px; height: 203px; }
  .card--back-land  { left: 423px; top: 63px; width: 360px; height: 203px; }
  .card--front-port { left: 199px; top: 344px; width: 206px; height: 357px; }
  .card--back-port  { left: 444px; top: 344px; width: 206px; height: 357px; }
  .card svg { position: absolute; inset: 0; width: 100%; height: 100%; }

  .photo { position: absolute; }
  .photo--spill-land {
    left: 20px; top: 0; width: 300px; height: 203px;
    background: radial-gradient(closest-side at 55% 55%, var(--orchid) 0%, var(--orchid-soft) 50%, rgba(241,241,242,0) 100%);
    opacity: .75;
  }
  .photo--bottles-land {
    left: 110px; top: 0; width: 250px; height: 203px;
    background: radial-gradient(closest-side at 65% 75%, var(--orchid) 0%, var(--orchid-soft) 50%, rgba(241,241,242,0) 100%);
    opacity: .6;
  }
  .photo--spill-port {
    left: 0; top: 10px; width: 206px; height: 255px;
    background: radial-gradient(closest-side at 50% 48%, var(--orchid-deep) 0%, var(--orchid) 40%, var(--orchid-soft) 70%, rgba(241,241,242,0) 100%);
  }
  .photo--bottles-port {
    left: 0; top: 10px; width: 206px; height: 225px;
    background: radial-gradient(closest-side at 58% 62%, var(--orchid) 0%, var(--orchid-soft) 50%, rgba(241,241,242,0) 100%);
  }

  .brand-name { fill: var(--white); font-family: "Arimo", Arial, sans-serif; font-weight: 400; }
  .band-text { fill: var(--white); font-family: "Arimo", Arial, sans-serif; font-weight: 700; }
  .small-line { fill: var(--ink); font-family: "Arimo", Arial, sans-serif; }

  .band {
    position: absolute; left: 0; width: 100%; height: 46px; top: 261px;
    background: var(--plum); color: var(--white);
    display: flex; align-items: center;
  }
  .band--logo { justify-content: flex-end; padding-right: 16px; }
  .band--call { justify-content: center; font-size: 12px; }
  .address-block {
    position: absolute; left: 0; top: 232px; width: 100%;
    text-align: center; color: var(--ink);
    font-weight: 700; font-size: 11px; line-height: 12px;
  }
  .fine-print {
    position: absolute; left: 0; top: 311px; width: 100%;
    text-align: center; color: var(--fine-ink);
    font-family: "Tinos", "Times New Roman", serif; font-size: 6.5px; line-height: 9px;
  }
  .brand-stack { display: flex; align-items: flex-end; gap: 4px; line-height: 1; }
  .brand-stack .brand-word { font-size: 28px; }
  .brand-stack .brand-sub { font-size: 9px; padding-bottom: 3px; }
</style>
</head>
<body>
<main class="sheet">

  <section class="card card--front-land">
    <div class="photo photo--spill-land" role="img" aria-label="Spilled purple nail polish bottle with crushed glitter powder"></div>
    <svg viewBox="0 0 360 203">
      <polygon points="0,64 360,25 360,80 0,128" fill="var(--plum)"/>
      <polygon points="0,133 360,88 360,113 0,152" fill="var(--charcoal)"/>
      <g transform="rotate(-6.2 180 100)">
        <text class="brand-name" x="40" y="100" font-size="36">Lumen</text>
        <text class="brand-name" x="140" y="127" font-size="11">Nail Designs</text>
      </g>
    </svg>
  </section>

  <section class="card card--back-land">
    <div class="photo photo--bottles-land" role="img" aria-label="Upright nail polish bottle with brush and a tipped pink bottle spilling polish"></div>
    <svg viewBox="0 0 360 203">
      <polygon points="0,58 360,4 360,98 0,133" fill="var(--plum)"/>
      <polygon points="0,133 360,98 360,107 0,142" fill="var(--charcoal)"/>
      <g transform="rotate(-6.3 180 95)">
        <text class="band-text" x="180" y="76" font-size="12.5" text-anchor="middle">41 Wendover street, Carrowbrook,</text>
        <text class="band-text" x="180" y="91" font-size="12.5" text-anchor="middle">NSW 2791</text>
        <text class="band-text" x="180" y="106" font-size="12.5" text-anchor="middle">Mobile: 0400 582 316</text>
        <text class="small-line" x="352" y="138" text-anchor="end" font-size="8">Tessa Harcourt Like us on Chatterly</text>
        <text class="small-line" x="8" y="137" font-size="8">Appointment timings:</text>
      </g>
    </svg>
  </section>

  <section class="card card--front-port">
    <div class="photo photo--spill-port" role="img" aria-label="Spilled dark purple nail polish bottle with crushed glitter powder"></div>
    <div class="band band--logo">
      <div class="brand-stack">
        <span class="brand-word">Lumen</span>
        <span class="brand-sub">Nail Designs</span>
      </div>
    </div>
  </section>

  <section class="card card--back-port">
    <div class="photo photo--bottles-port" role="img" aria-label="Upright nail polish bottle with brush and a tipped pink bottle spilling polish"></div>
    <p class="address-block">41 Wendover street, Carrowbrook,<br>NSW 2791</p>
    <div class="band band--call">Call on: 0400 582 316</div>
    <p class="fine-print">Tessa Harcourt Like us on Chatterly<br>Appointment timings:</p>
  </section>

</main>
</body>
</html>
```